BrambleWorks business card

Looking for business card design that supports our company/software values. We have 2 logo designs at the moment but open to change if you think you can enhance the brand. Check out website www.brambleworks.com.au.

Target Market(s)

Education

Contact Information for Business Card

Name, title, mobile, email and website

Font styles to use
Sans Serif

Colors

Designer to choose colors to be used in the design.

Requirements
Must have
• BrambleWorks logo with tree and tagline on rear side with dark grey background colour

```html
<!DOCTYPE html>
<html lang="en">
<head>
<meta charset="utf-8">
<title>BrambleWorks business card</title>
<link href="https://fonts.googleapis.com/css2?family=Open+Sans:wght@400;600;700&display=swap" rel="stylesheet">
<style>
:root{
  --backdrop:#2d2e2f;
  --brand-green:#3b6d35;
  --ink-grey:#4a4a4a;
  --rule-grey:#555555;
  --card-white:#ffffff;
}
*{box-sizing:border-box;margin:0;padding:0}
html,body{width:1200px;height:900px;overflow:hidden}
body{background:var(--backdrop);font-family:"Open Sans",sans-serif;position:relative}
.card{position:absolute;left:310px;width:580px;height:330px;border-radius:22px;overflow:hidden}
.card--rear{top:80px;background:var(--brand-green);color:var(--card-white)}
.card--front{top:470px;background:var(--card-white);color:var(--ink-grey)}
.brand{position:absolute;display:flex;flex-direction:column}
.brand__row{display:flex;align-items:center}
.brand__dot{border-radius:50%;flex:none}
.brand__name{font-weight:600;line-height:1;white-space:nowrap}
.brand__rule{height:1.5px;margin:8px 0 4px}
.brand__tagline{font-weight:400;white-space:nowrap}
.card--rear .brand{left:100px;top:108px}
.card--rear .brand__row{gap:14px}
.card--rear .brand__dot{width:62px;height:62px;background:var(--card-white)}
.card--rear .brand__name{font-size:50px}
.card--rear .brand__rule{background:var(--card-white);margin-left:76px}
.card--rear .brand__tagline{font-size:20px;margin-left:76px}
.card--front .brand{left:34px;top:100px}
.card--front .brand__row{gap:10px}
.card--front .brand__dot{width:28px;height:28px;background:var(--ink-grey)}
.card--front .brand__name{font-size:26px}
.card--front .brand__rule{background:var(--ink-grey);margin:6px 0 3px 38px}
.card--front .brand__tagline{font-size:11.5px;margin-left:38px}
.divider{position:absolute;left:300px;top:70px;width:1.5px;height:170px;background:var(--brand-green)}
.contact{position:absolute;left:322px;top:66px;font-size:14px;line-height:1.3}
.contact__name{color:var(--brand-green);font-weight:700;font-size:21px;line-height:1.1}
.contact__title{font-size:18px;margin-bottom:6px}
.contact__address{margin-bottom:4px}
.contact__list{list-style:none}
.contact__list li{display:flex;align-items:center;gap:8px;height:20px}
.contact__list svg{width:13px;height:13px;flex:none}
.band{position:absolute;left:0;bottom:0;width:580px;height:110px}
</style>
</head>
<body>
<section class="card card--rear">
  <div class="brand">
    <div class="brand__row"><span class="brand__dot"></span><span class="brand__name">BrambleWorks</span></div>
    <div class="brand__rule"></div>
    <div class="brand__tagline">Student Success Platform</div>
  </div>
</section>

<section class="card card--front">
  <div class="brand">
    <div class="brand__row"><span class="brand__dot"></span><span class="brand__name">BrambleWorks</span></div>
    <div class="brand__rule"></div>
    <div class="brand__tagline">Student Success Platform</div>
  </div>
  <div class="divider"></div>
  <div class="contact">
    <div class="contact__name">Marten Olsen</div>
    <div class="contact__title">Doctor</div>
    <div class="contact__address">4820 Ashgrove Lane, Suite 210<br>Fairview Park, OH 44126</div>
    <ul class="contact__list">
      <li><svg viewBox="0 0 16 16"><path d="M4 1l3 3-2 2c1 2 3 4 5 5l2-2 3 3-2 3C7 15 1 9 2 3z" fill="#3b6d35"/></svg>216-555-0142</li>
      <li><svg viewBox="0 0 16 16"><rect x="4" y="1" width="8" height="4" fill="#3b6d35"/><rect x="1" y="6" width="14" height="6" rx="1" fill="#3b6d35"/><rect x="4" y="10" width="8" height="5" fill="#3b6d35" stroke="#fff"/></svg>216-555-0187</li>
      <li><svg viewBox="0 0 16 16"><rect x="1" y="3" width="14" height="10" fill="#3b6d35"/><path d="M1 3l7 6 7-6" fill="none" stroke="#fff" stroke-width="1.4"/></svg>info@brambleworks.com.au</li>
      <li><svg viewBox="0 0 16 16"><circle cx="8" cy="8" r="7" fill="#3b6d35"/><path d="M1 8h14M8 1v14M3 4h10M3 12h10" stroke="#fff" stroke-width="0.8"/></svg>www.brambleworks.com.au</li>
    </ul>
  </div>
  <svg class="band" viewBox="0 0 580 110" preserveAspectRatio="none">
    <path d="M0 20 Q300 110 580 95 L580 110 L0 110 Z" fill="#3b6d35"/>
    <path d="M0 8 Q300 95 580 82" fill="none" stroke="#555555" stroke-width="3"/>
  </svg>
</section>
</body>
</html>
```